Tarrow Building Ventures needs a Business card design and logo

We Need a business card design and logo for a Building & Construction business based in Melbourne. We work in both the Domestic & Commercial sector. We specialize in all aspects of building including extensions, Renovations, and alterations. Construction Management, Project Management, And labour hire
Updates

Industry/Entity Type

Business

```html
<!DOCTYPE html>
<html lang="en">
<head>
<meta charset="utf-8">
<title>Tarrow Building Ventures – Business Card</title>
<link href="https://fonts.googleapis.com/css2?family=Open+Sans:wght@400;600;700&family=Oswald:wght@400;500&display=swap" rel="stylesheet">
<style>
  :root {
    --page-bg: #e9e9ea;
    --card-white: #ffffff;
    --card-fade: #e4e5e7;
    --brand-blue: #1f8fd6;
    --brand-blue-dark: #1676b6;
    --charcoal: #333436;
    --mid-grey: #c9cacc;
    --text-dark: #2b2c2e;
    --text-light: #ffffff;
  }
  * { box-sizing: border-box; margin: 0; padding: 0; }
  html, body { width: 1057px; height: 1200px; overflow: hidden; }
  body {
    background: var(--page-bg);
    font-family: "Open Sans", Arial, sans-serif;
    position: relative;
  }
  .card {
    position: absolute;
    left: 98px;
    width: 860px;
    height: 491px;
    overflow: hidden;
    box-shadow: 0 6px 18px rgba(0,0,0,.18);
  }
  .card--front { top: 60px; background: var(--brand-blue); }
  .card--back { top: 640px; background: radial-gradient(ellipse at 40% 30%, var(--card-white) 40%, var(--card-fade) 100%); }

  /* front */
  .front-frame {
    position: absolute; inset: 18px;
    background: var(--charcoal);
  }
  .front-panel {
    position: absolute; inset: 14px;
    background: radial-gradient(ellipse at center, var(--card-white) 35%, var(--card-fade) 100%);
    display: flex; flex-direction: column; align-items: center; justify-content: center;
  }
  .brand {
    display: flex; align-items: center; gap: 14px;
  }
  .brand-square {
    width: 34px; height: 34px; background: var(--brand-blue); flex: none;
  }
  .brand-name {
    font-weight: 700; color: var(--brand-blue-dark);
    font-size: 40px; letter-spacing: .5px; white-space: nowrap;
  }
  .brand-tagline {
    margin-top: 10px; font-size: 15px; color: var(--text-dark);
    border-top: 2px solid var(--charcoal); padding-top: 6px;
  }

  /* back */
  .back-brand {
    position: absolute; left: 150px; top: 70px;
    display: flex; flex-direction: column; align-items: flex-start;
  }
  .back-brand .brand-name { font-size: 30px; }
  .back-brand .brand-square { width: 26px; height: 26px; }
  .back-brand .brand-tagline { font-size: 12px; }

  .phone-band {
    position: absolute; right: 0; top: 190px; width: 360px; height: 56px;
    background: var(--charcoal);
    clip-path: polygon(40px 0, 100% 0, 100% 100%, 0 100%);
  }
  .phone-strip {
    position: absolute; right: 0; top: 246px; width: 330px; height: 66px;
    background: var(--mid-grey);
    clip-path: polygon(34px 0, 100% 0, 100% 100%, 0 100%);
    display: flex; flex-direction: column; justify-content: center; gap: 8px;
    padding-left: 60px;
  }
  .contact-row {
    display: flex; align-items: center; gap: 10px;
    font-size: 13px; color: var(--text-dark); white-space: nowrap;
  }
  .icon-box {
    width: 18px; height: 18px; background: var(--brand-blue);
    display: flex; align-items: center; justify-content: center; flex: none;
  }
  .icon-box svg { width: 11px; height: 11px; fill: var(--text-light); }

  .name-panel {
    position: absolute; left: 0; bottom: 120px; width: 470px; height: 110px;
    background: linear-gradient(90deg, var(--brand-blue-dark), var(--brand-blue));
    clip-path: polygon(0 0, 88% 0, 100% 100%, 0 100%);
    padding: 22px 0 0 46px; color: var(--text-light);
  }
  .person-name { font-family: "Oswald", Arial, sans-serif; font-weight: 500; font-size: 38px; letter-spacing: 2px; line-height: 1; }
  .person-role { font-family: "Oswald", Arial, sans-serif; font-weight: 400; font-size: 20px; letter-spacing: 3px; margin-top: 6px; }

  .details-band {
    position: absolute; left: 0; bottom: 0; width: 560px; height: 120px;
    background: var(--charcoal);
    clip-path: polygon(0 0, 92% 0, 100% 100%, 0 100%);
    display: flex; flex-direction: column; justify-content: center; gap: 10px;
    padding-left: 46px;
  }
  .details-band .contact-row { color: var(--text-light); }
</style>
</head>
<body>
  <section class="card card--front" aria-label="Card front">
    <div class="front-frame">
      <div class="front-panel">
        <div class="brand">
          <span class="brand-square"></span>
          <span class="brand-name">Tarrow Building Ventures</span>
        </div>
        <p class="brand-tagline">Building Extensions, Renovations &amp; Alterations</p>
      </div>
    </div>
  </section>

  <section class="card card--back" aria-label="Card back">
    <div class="back-brand">
      <div class="brand">
        <span class="brand-square"></span>
        <span class="brand-name">Tarrow Building Ventures</span>
      </div>
      <p class="brand-tagline">Building Extensions, Renovations &amp; Alterations</p>
    </div>

    <div class="phone-band"></div>
    <div class="phone-strip">
      <div class="contact-row">
        <span class="icon-box"><svg viewBox="0 0 24 24"><path d="M6.6 10.8a15 15 0 0 0 6.6 6.6l2.2-2.2c.3-.3.7-.4 1-.2 1.1.4 2.3.6 3.6.6.6 0 1 .4 1 1V20c0 .6-.4 1-1 1A17 17 0 0 1 3 4c0-.6.4-1 1-1h3.5c.6 0 1 .4 1 1 0 1.3.2 2.5.6 3.6.1.3 0 .7-.2 1z"/></svg></span>
        <span>047 812 3305</span>
      </div>
      <div class="contact-row">
        <span class="icon-box"><svg viewBox="0 0 24 24"><path d="M7 2h10a2 2 0 0 1 2 2v16a2 2 0 0 1-2 2H7a2 2 0 0 1-2-2V4a2 2 0 0 1 2-2zm0 3v13h10V5z"/></svg></span>
        <span>047 812 3306</span>
      </div>
    </div>

    <div class="name-panel">
      <p class="person-name">OWEN HALE</p>
      <p class="person-role">FOUNDER</p>
    </div>

    <div class="details-band">
      <div class="contact-row">
        <span class="icon-box"><svg viewBox="0 0 24 24"><path d="M12 2a7 7 0 0 0-7 7c0 5 7 13 7 13s7-8 7-13a7 7 0 0 0-7-7zm0 9.5A2.5 2.5 0 1 1 12 6.5a2.5 2.5 0 0 1 0 5z"/></svg></span>
        <span>27 Harbour View Road Melbourne</span>
      </div>
      <div class="contact-row">
        <span class="icon-box"><svg viewBox="0 0 24 24"><path d="M3 5h18v14H3zm2 2v.5l7 4.5 7-4.5V7z"/></svg></span>
        <span>info@tarrowbuild.com</span>
      </div>
      <div class="contact-row">
        <span class="icon-box"><svg viewBox="0 0 24 24"><path d="M12 2a10 10 0 1 0 0 20 10 10 0 0 0 0-20zm0 2c1 1.3 1.8 3.3 2 6H10c.2-2.7 1-4.7 2-6zm-2 8h4c-.2 2.7-1 4.7-2 6-1-1.3-1.8-3.3-2-6z"/></svg></span>
        <span>www.tarrowbuild.com</span>
      </div>
    </div>
  </section>
</body>
</html>
```